Political themed graphic for contemporary church sermon series

Contemporary church in California need a graphic design for a sermon series. The sermon series will be focused on the upcoming presidential election. The sermon series is titled for the question "who will be the next president":

Title: 45
Subtitle: Who will it be / Does it matter

The design should use red, white and blue and should possibly have the cedar hall in the graphic somewhere. Maybe like a watermark or something to that effect.

Target Market(s)

Contemporary design,

Industry/Entity Type

Church

Font styles to use
Serif
Sans Serif

Colors
0555a3
ec1f27
ffffff

Requirements
Must have
• Political theme, red, white and blue (contemporary color palette). Cedar hall screened back in the design somewhere.
• the title large: 45
• and subtitle: Who will it be | Does it matter
Should not have
• I'm not looking for cheesy graphics with elephant and a donkey.

```html
<!DOCTYPE html>
<html lang="en">
<head>
<meta charset="utf-8">
<title>45 — Who Will It Be / Does It Matter</title>
<link rel="stylesheet" href="https://fonts.googleapis.com/css2?family=Antonio:wght@600&display=swap">
<style>
  :root {
    --backdrop: #ececec;
    --navy: #143a73;
    --crimson: #cb0a3c;
    --white: #ffffff;
  }
  html, body {
    margin: 0;
    padding: 0;
    width: 1200px;
    height: 1000px;
    overflow: hidden;
    background: var(--backdrop);
  }
  .stage {
    position: relative;
    width: 1200px;
    height: 1000px;
  }
  .series-banner {
    position: absolute;
    left: 100px;
    top: 308px;
    width: 1000px;
    height: 382px;
    box-shadow: 0 2px 6px rgba(0,0,0,0.18);
  }
  .panel-blue { fill: var(--navy); }
  .panel-red { fill: var(--crimson); }
  .divider { fill: var(--white); }
  .series-title,
  .series-question {
    fill: var(--white);
    font-family: "Antonio", "Arial Narrow", sans-serif;
    font-weight: 600;
    text-transform: uppercase;
  }
  .series-title { font-size: 325px; }
  .series-question { font-size: 127px; }
</style>
</head>
<body>
<main class="stage">
  <svg class="series-banner" viewBox="100 308 1000 382" width="1000" height="382" aria-labelledby="banner-title">
    <title id="banner-title">45 — Who will it be / Does it matter</title>
    <rect class="panel-blue" x="100" y="308" width="383" height="382"/>
    <rect class="divider" x="483" y="308" width="16" height="382"/>
    <rect class="panel-red" x="499" y="308" width="601" height="382"/>

    <text class="series-title" x="152" y="640" textLength="280" lengthAdjust="spacingAndGlyphs">45</text>

    <text class="series-question" x="550" y="468" textLength="488" lengthAdjust="spacingAndGlyphs">Who will it be</text>
    <text class="series-question" x="550" y="640" textLength="500" lengthAdjust="spacingAndGlyphs">Does it matter</text>
  </svg>
</main>
</body>
</html>
```